Prescription Savings Card

Looking to revamp our cards that are distributed to pharmacies. Processing information must stand out and be in black with lines through zeros for easy identification.
I have included some previous card designs for consideration. we are looking to go with something cleaner with mainly processing information on the back similar to all white version attached.
Target Market(s)
Pharmacists and Pharmacy Technicians
Industry/Entity Type
prescription medications
Contact Information for Business Card
processing information
Requirements
Must have
- easy to read processing information

```html
<!DOCTYPE html>
<html lang="en">
<head>
<meta charset="utf-8">
<title>Medvance Prescription Savings Card</title>
<link rel="stylesheet" href="https://fonts.googleapis.com/css2?family=Montserrat:wght@400;500;700;800&display=swap">
<style>
  :root {
    --backdrop: #3a3a3c;
    --card-white: #ffffff;
    --navy: #2e2b80;
    --navy-band: #34457a;
    --red: #e10916;
    --ink: #111111;
    --rule: #3b4a7e;
  }
  * { margin: 0; padding: 0; box-sizing: border-box; }
  html, body {
    width: 1200px; height: 1200px; overflow: hidden;
    background: var(--backdrop);
    font-family: "Montserrat", sans-serif;
  }
  .canvas { position: relative; width: 1200px; height: 1200px; }
  .card {
    position: absolute; left: 150px;
    width: 900px; height: 514px;
    border-radius: 36px; overflow: hidden;
    box-shadow: 0 18px 40px rgba(0,0,0,0.45);
  }

  /* Processing side */
  .card--processing { top: 60px; background: var(--card-white); color: var(--ink); }
  .brand-name {
    position: absolute; right: 60px; top: 40px;
    font-weight: 800; font-size: 64px; letter-spacing: -2px;
    color: var(--navy);
  }
  .processing-grid {
    position: absolute; left: 70px; top: 140px;
    display: grid; grid-template-columns: 300px auto;
    row-gap: 6px; font-size: 36px; line-height: 44px;
  }
  .processing-label { font-weight: 700; letter-spacing: 1px; }
  .processing-value { font-weight: 400; letter-spacing: 2px; }
  .rule {
    position: absolute; left: 230px; right: 50px; height: 1px;
    background: var(--rule);
  }
  .rule--top { top: 345px; }
  .rule--bottom { top: 448px; }
  .service-info {
    position: absolute; left: 230px; right: 50px; top: 360px;
    text-align: center; line-height: 36px;
  }
  .service-phone { font-size: 26px; letter-spacing: 1px; }
  .service-note { font-size: 22px; letter-spacing: 1px; }
  .band {
    position: absolute; bottom: 0; height: 30px;
  }
  .band--red { left: 0; width: 58%; background: var(--red); }
  .band--navy { right: 0; width: 41%; background: var(--navy-band); }

  /* Promo side */
  .card--promo { top: 626px; background: var(--navy); color: #ffffff; }
  .promo-tagline {
    position: absolute; left: 150px; top: 120px;
    font-weight: 700; font-size: 38px; letter-spacing: 3px;
  }
  .promo-brand {
    position: absolute; left: 130px; top: 170px;
    font-weight: 800; font-size: 130px; letter-spacing: -4px; line-height: 1;
    color: #ffffff;
  }
  .promo-pricing {
    position: absolute; left: 300px; top: 345px;
    font-weight: 500; font-size: 26px; letter-spacing: 1px;
  }
  .promo-url {
    position: absolute; left: 300px; top: 385px; width: 480px;
    text-align: center; font-weight: 500; font-size: 30px;
  }
  .promo-bar {
    position: absolute; left: 400px; right: 0; top: 452px; height: 28px;
    background: var(--red);
  }
</style>
</head>
<body>
<main class="canvas">
  <section class="card card--processing" aria-label="Processing information side">
    <div class="brand-name">Medvance</div>
    <dl class="processing-grid">
      <dt class="processing-label">BIN:</dt><dd class="processing-value">000000</dd>
      <dt class="processing-label">ID:</dt><dd class="processing-value">MDVANCE</dd>
      <dt class="processing-label">PCN:</dt><dd class="processing-value">RX000</dd>
      <dt class="processing-label">GROUP:</dt><dd class="processing-value">RX00000</dd>
    </dl>
    <div class="rule rule--top"></div>
    <div class="service-info">
      <p class="service-phone">Customer Service (866)-555-0148</p>
      <p class="service-note">This is NOT INSURANCE</p>
    </div>
    <div class="rule rule--bottom"></div>
    <div class="band band--red"></div>
    <div class="band band--navy"></div>
  </section>

  <section class="card card--promo" aria-label="Promotional side">
    <p class="promo-tagline">PRESCRIPTIONS AT A DISCOUNT</p>
    <div class="promo-brand">Medvance</div>
    <p class="promo-pricing">Check Current Pricing on our Website</p>
    <p class="promo-url">Medvance.com</p>
    <div class="promo-bar"></div>
  </section>
</main>
</body>
</html>
```